Retirement Plan Advisor Bio

See the attached document and photo for content. I would like someone to design this one page flyer using my logo. This logo was designed by a designer with sketch hive. I am looking for a professional looking document. I want to he color scheme to be primarily white and gold.

Target Market(s)

Employers who offer a retirement plan

Requirements
Should not have
• The designs that I have received look more like resumes. I am interested in advertising my Retirement plan services. If anyone can change their submissions and change it to an ad for retirement plan services instead of a Bio or resume, I would prefer that.

```html
<!DOCTYPE html>
<html lang="en">
<head>
<meta charset="utf-8">
<title>Retirement Plan Services – Helen R Ashby</title>
<link rel="stylesheet" href="https://fonts.googleapis.com/css2?family=Roboto+Condensed:ital,wght@1,300;1,400&family=Roboto:wght@400&display=swap">
<style>
  :root {
    --gold: #a6843f;
    --white: #ffffff;
    --ink: #1a1a1a;
    --photo-bg: #7d8fa8;
  }
  * { margin: 0; padding: 0; box-sizing: border-box; }
  html, body { width: 849px; height: 1200px; overflow: hidden; background: var(--white); }
  .flyer { position: relative; width: 849px; height: 1200px; background: var(--white); color: var(--ink); }

  .headline-band {
    position: absolute; left: 32px; top: 28px; width: 793px; height: 232px;
    background: var(--gold); color: var(--white);
    display: flex; align-items: center; justify-content: center; text-align: center;
  }
  .headline {
    font-family: "Roboto Condensed", "Arial Narrow", sans-serif;
    font-style: italic; font-weight: 300; font-size: 38px; line-height: 36.6px;
    letter-spacing: -0.4px; margin-top: -6px;
  }

  .pitch {
    position: absolute; left: 97px; top: 294px; width: 700px;
    font-family: "Roboto Condensed", "Arial Narrow", sans-serif;
    font-style: italic; font-weight: 300; font-size: 27.6px; line-height: 28.7px;
  }
  .services {
    position: absolute; left: 93px; top: 388px; width: 720px; list-style: none;
    font-family: "Roboto Condensed", "Arial Narrow", sans-serif;
    font-style: italic; font-weight: 300; font-size: 27.6px; line-height: 45.7px;
  }
  .services li { position: relative; padding-left: 18px; }
  .services li::before {
    content: ""; position: absolute; left: 0; top: 18px;
    width: 12.5px; height: 12.5px; border-radius: 50%; background: var(--gold);
  }

  .divider { position: absolute; left: 32px; top: 661px; width: 793px; height: 6px; background: var(--gold); }

  .portrait {
    position: absolute; left: 49px; top: 720px; width: 266px; height: 266px; border-radius: 50%;
    background: radial-gradient(circle at 50% 45%, #d9b79a 0%, #c9a77a 30%, var(--photo-bg) 70%);
  }

  .advisor {
    position: absolute; left: 40px; top: 996px; width: 284px; text-align: center;
    font-family: "Roboto", Arial, sans-serif; font-size: 16.5px; line-height: 20px; color: var(--gold);
  }

  .firm {
    position: absolute; left: 341px; top: 746px; display: flex; align-items: center; gap: 14px;
    font-family: "Roboto", Arial, sans-serif; font-size: 30px; line-height: 40px; color: var(--gold);
  }
  .firm-mark { width: 40px; height: 40px; background: var(--gold); }

  .credentials {
    position: absolute; left: 367px; top: 810px; list-style: none;
    font-family: "Roboto", Arial, sans-serif; font-size: 17px; line-height: 31.2px; color: var(--ink);
  }

  .disclosure {
    position: absolute; left: 32px; top: 1065px; width: 793px; text-align: center;
    font-family: "Roboto", Arial, sans-serif; font-size: 13.3px; line-height: 21px;
  }

  .contact-band {
    position: absolute; left: 32px; top: 1115px; width: 793px; height: 41px;
    background: var(--gold); color: var(--white);
    display: flex; align-items: center; justify-content: space-between; padding: 0 22px 0 14px;
    font-family: "Roboto", Arial, sans-serif; font-size: 16px;
  }
</style>
</head>
<body>
<main class="flyer">
  <header class="headline-band">
    <h1 class="headline">I can help you reduce your<br>ADMINISTRATIVE BURDEN and<br>FUDICIARY RISK, while at the same time<br>IMPROVE your employee's RETIREMENT<br>OUTCOMES.</h1>
  </header>

  <p class="pitch">In my 18 years in the retirement plan industry, I have helped<br>hundreds of employers and their employees achieve just that<br>through a system that consists of:</p>
  <ul class="services">
    <li>careful retirement planning design by analysing their savings<br>rate, investment strategy and overall financial wellness</li>
    <li>strategic and targeted communication</li>
    <li>education</li>
    <li>and continual monitoring of results.</li>
  </ul>

  <div class="divider"></div>

  <div class="portrait" role="img" aria-label="Portrait photograph of the advisor"></div>
  <p class="advisor">Helen R Ashby CRS APF<br>Northpeak Financial Advisor</p>

  <div class="firm"><span class="firm-mark"></span><span>Verra Financial, LLC</span></div>
  <ul class="credentials">
    <li>Certified Retirement Strategist</li>
    <li>Accredited Plan Fiduciary</li>
    <li>Investment Advisor Representative</li>
    <li>Series 7, 63, and 65 Securities licenses with Northpeak</li>
    <li>Holds Life and Health Insurance licenses from Illinois</li>
    <li>BS Westbrook University, 1987</li>
  </ul>

  <p class="disclosure">*Securities and Investment Advisory Services offered through Northpeak Holdings, Inc,<br>a Registered Broker/Dealer and Investment Advisor, member SRG/IPT</p>

  <footer class="contact-band">
    <span>250 Harmon Ave. Lakeview, IL 60999 (555)014.2287</span>
    <span>helen.ashby@northpeak.com</span>
    <span>www.helenashby.com</span>
  </footer>
</main>
</body>
</html>
```